Our company TrulaPay, an online processor of payments is seeking talented submissions for our website redesign. The winning design will be chopped up and converted into a WordPress theme to allow for easy content additions and updates.

We are looking for modern designs that rival current websites in our industry (plimo.example, zanquetto.example, holvix.example, brandle.example, quillmarkcharges.example, evensplitcharges.example, KoboRun.example).

Our company is seeking to expand our reach to software developers and engineers who are either integrating our payment platform into their offerings or are engineering a custom solution for the company they work for and are in need of a payment platform such as our own.

We currently work with hundreds of different business partners whom either resell our services or integrate our processing capabilities into their software (which they sell). We also must communicate effectively to end users, businesses, who seek us out directly for their payment processing needs.

We are open to different color schemes but would ultimately like them to be somewhat inline with our current logo (see attached). Our website needs to instill security and confidence to any current and/or potential user as we are trusted with private and sensitive information.

We are seeking submissions from qualified; individual freelancers, freelance teams, and agencies who can attack this project in its entirety. Since this project is a total redesign, we would like submissions that have the capability to design any custom graphics, icons, buttons, and illustrations in line with our industry, capabilities, offerings, and content. We are looking for someone to design our new website and would prefer a vendor who can also help us to design elements (graphics, illustrations, charts, workflows) within our website.

Designs will be converted into a wordpress theme and we would like to utilize widgets for as many areas as possible to make editing and updating easy.

We are seeking the creation of a few unique pages but many of the pages for the majority of our content will just be internal content pages which will be duplicated.

We will likely contract with the winning submission for future work.

Please see Design Reference Document for more information

Target Market(s)

Resellers
Merchant Service Providers
Software Developers
Independent Sales Organizations (ISOs)
App Builders
Mobile App Builders
Independent Software Developers
Organizational Software Developers
Businesses who need to accept payments
Governments
Municipalities
Schools
DMVs
Courts
Retailers
Medical Offices
Hosipitals
Clinics
Dr. Offices
Gyms
Churches
Non-Profits
Software Companies
Technology Companies
Startups

• Logo cannot change drastically.

```html
<!DOCTYPE html>
<html lang="en">
<head>
<meta charset="utf-8">
<title>TrulaPay – Electronic ACH Processing</title>
<link href="https://fonts.googleapis.com/css2?family=Tinos:wght@400;700&display=swap" rel="stylesheet">
<style>
  :root {
    --brand-blue: #0a0a9c;
    --brand-red: #e4000f;
    --ink: #222;
    --body-text: #555;
    --muted: #888;
    --nav-bg: #2c2c2c;
    --footer-bg: #2a2a2a;
    --rule: #dcdcdc;
    --white: #fff;
  }
  * { box-sizing: border-box; margin: 0; padding: 0; }
  html, body { width: 1158px; height: 1200px; overflow: hidden; }
  body { font-family: "Tinos", "Times New Roman", serif; color: var(--ink); background: var(--white); position: relative; }

  .site-header { position: absolute; top: 0; left: 0; width: 1158px; height: 86px; }
  .brand { position: absolute; left: 194px; top: 10px; }
  .brand-powered { font-size: 13px; font-weight: 700; color: #111; }
  .brand-name { display: flex; align-items: center; gap: 6px; margin-top: 2px; }
  .brand-name .mark { width: 12px; height: 12px; border-radius: 50%; background: var(--brand-red); }
  .brand-name span { font-size: 28px; color: var(--brand-blue); line-height: 1; }
  .brand-tag { font-size: 9px; font-weight: 700; color: #111; margin-left: 70px; margin-top: 2px; }
  .help-line { position: absolute; left: 688px; top: 29px; }
  .help-line small { display: block; font-size: 7.5px; color: #222; }
  .help-line strong { display: block; font-size: 21px; font-weight: 400; color: #111; line-height: 1; }
  .btn-head { position: absolute; top: 29px; height: 27px; color: var(--white); font-size: 13px; display: flex; align-items: center; justify-content: center; }
  .btn-email { left: 818px; width: 102px; background: var(--brand-blue); }
  .btn-login { left: 902px; width: 64px; background: var(--brand-red); left: 902px; }
  .btn-email { left: 818px; width: 80px; }

  .main-nav { position: absolute; top: 86px; left: 0; width: 1158px; height: 39px; background: var(--nav-bg); }
  .main-nav ul { list-style: none; position: absolute; left: 193px; top: 0; display: flex; height: 39px; align-items: center; }
  .main-nav li { color: #c8c8c8; font-size: 12px; margin-right: 34px; }
  .search { position: absolute; left: 745px; top: 6px; width: 221px; height: 27px; background: #3c3c3c; border: 1px solid #4a4a4a; color: #888; font-size: 10px; padding: 7px 6px; }
  .search svg { position: absolute; right: 6px; top: 5px; }

  .hero { position: absolute; top: 125px; left: 0; width: 1158px; height: 354px; background: linear-gradient(#fff 0%, #f2f2f2 50%, #e3e3e3 100%); }
  .hero-card { position: absolute; top: 31px; width: 380px; height: 276px; color: var(--white); padding: 10px 12px; box-shadow: 0 14px 12px -10px rgba(0,0,0,.35); }
  .card-business { left: 193px; background: radial-gradient(circle at 45% 30%, #8a8a98 0%, #3b3f62 40%, #1a1f44 80%); }
  .card-dev { left: 586px; background: radial-gradient(circle at 60% 60%, #f2627a 0%, #d42848 45%, #9a0a20 90%); }
  .hero-card h2 { font-size: 17px; line-height: 21px; font-weight: 700; padding-bottom: 8px; border-bottom: 1px dashed rgba(255,255,255,.6); }
  .hero-card p { font-size: 11px; line-height: 17px; margin-top: 18px; }
  .hero-btn { position: absolute; left: 98px; top: 216px; width: 184px; height: 38px; background: var(--white); font-size: 15px; display: flex; align-items: center; justify-content: center; box-shadow: 0 1px 3px rgba(0,0,0,.3); }
  .card-business .hero-btn { color: #1b2040; }
  .card-dev .hero-btn { color: #b0101e; }

  .welcome { position: absolute; top: 505px; left: 193px; width: 523px; }
  .welcome h2 { font-size: 17px; color: var(--brand-blue); font-weight: 700; }
  .welcome p { font-size: 11px; line-height: 16.2px; color: var(--body-text); margin-top: 5px; }
  .welcome p + p { margin-top: 0; }
  .industries { position: absolute; top: 509px; left: 727px; width: 205px; height: 190px; border-left: 1px solid var(--rule); padding-left: 12px; }
  .industries h2 { font-size: 17px; color: var(--brand-red); font-weight: 700; margin-top: -4px; }
  .industries ul { list-style: none; margin-top: 6px; }
  .industries li { font-size: 11px; color: var(--body-text); height: 24.8px; line-height: 24px; border-bottom: 1px solid var(--rule); padding-left: 12px; position: relative; }
  .industries li:last-child { border-bottom: 0; }
  .industries li::before { content: ""; position: absolute; left: 1px; top: 11px; width: 3px; height: 3px; border-radius: 50%; background: #999; }

  .divider { position: absolute; top: 728px; left: 0; width: 1158px; height: 1px; background: var(--rule); }
  .intro { position: absolute; top: 746px; left: 240px; width: 678px; text-align: center; }
  .intro h1 { font-size: 30px; color: var(--brand-blue); font-weight: 700; line-height: 1.1; }
  .intro .lead { font-size: 11.5px; font-weight: 700; color: #222; margin-top: 3px; }
  .intro p { font-size: 10.5px; line-height: 12.5px; color: var(--body-text); margin-top: 13px; }
  .intro p + p { margin-top: 5px; }

  .ach { position: absolute; top: 884px; left: 193px; width: 773px; }
  .ach h2 { font-size: 17px; color: var(--brand-blue); font-weight: 700; }
  .ach-cols { display: flex; gap: 26px; margin-top: 14px; }
  .ach-col { width: 241px; }
  .ach-col h3 { font-size: 15px; font-weight: 400; color: #222; }
  .ach-photo { height: 131px; margin-top: 5px; border: 2px solid #e0e0e0; }
  .photo-gateway { background: linear-gradient(120deg, #e8d2c2, #f6f2ee 60%, #d6d9c8); }
  .photo-api { background: linear-gradient(120deg, #9fa6ae, #dfe3e6 50%, #8e8a86); }
  .photo-dev { background: linear-gradient(120deg, #d9b9a4, #efe5ee 55%, #2a2a2a 75%); }
  .ach-col p { font-size: 11px; line-height: 15px; color: var(--body-text); margin-top: 5px; }

  .site-footer { position: absolute; top: 1152px; left: 0; width: 1158px; height: 48px; background: var(--footer-bg); }
  .site-footer p { position: absolute; left: 194px; top: 18px; font-size: 8.5px; color: #777; }
  .socials { position: absolute; right: 192px; top: 12px; display: flex; gap: 7px; }
  .socials span { width: 24px; height: 24px; border-radius: 50%; background: #555; display: block; }
</style>
</head>
<body>
  <header class="site-header">
    <div class="brand">
      <div class="brand-powered">Powered By:</div>
      <div class="brand-name"><i class="mark"></i><span>TrulaPay</span></div>
      <div class="brand-tag">Electronic ACH Processing</div>
    </div>
    <div class="help-line"><small>If you need any help Call us on</small><strong>555-014-2290</strong></div>
    <a class="btn-head btn-email">Email Us</a>
    <a class="btn-head btn-login">Login</a>
  </header>

  <nav class="main-nav">
    <ul><li>Home</li><li>Solutions</li><li>Developers</li><li>Partners</li><li>Company</li><li>Resources</li><li>Blog</li></ul>
    <div class="search">Search
      <svg width="17" height="17" viewBox="0 0 17 17"><circle cx="7" cy="7" r="5.5" fill="none" stroke="#888" stroke-width="1.5"/><line x1="11" y1="11" x2="16" y2="16" stroke="#888" stroke-width="2"/></svg>
    </div>
  </nav>

  <section class="hero">
    <article class="hero-card card-business" role="img" aria-label="Blurred city skyline backdrop for businesses">
      <h2>Merchants, Businesses, I have a business, Online Payment Processing, SaaS</h2>
      <p>This interactive graphic box will convey to the website visitor that this is whereyou click if you are a business and need to get setup to accept payments for yourbusiness with us.Something along the lines of maybe some skyscrapers, maybe a business disctrict</p>
      <a class="hero-btn">Businesses Click Here</a>
    </article>
    <article class="hero-card card-dev" role="img" aria-label="Abstract red backdrop for developers">
      <h2>Developers, I Develop Software, Software Application Developers, Payment Processing API</h2>
      <p>Software Developers, Start-ups. Users who are looking to integrate a payment platform into their; website, ERP, CMS, mobile solution, software offering, sometype of advanced integration requiring a custom integration with a paymentprocessing platform, PaaS.<br>Something graphically that speaks to software engineers and developers. Initialthoughts were maybe some gears moving with source code or programming languages incorporated.</p>
      <a class="hero-btn">Devs Click Here</a>
    </article>
  </section>

  <section class="welcome">
    <h2>Wellcome To TrulaPay!</h2>
    <p>Lorem ipsum dolor sit amet, consectetur adipiscing elit. Etiam non arcu a sapien cursus sodales. Vivamus euismod dui at turpis lacinia non ultricies ipsum tincidunt. In hac habitasse platea dictumst. Nunc at velit quam. Vestibulum convallis cursus sodales. Donec purus sem, sodales faucibus malesuada et, feugiat id torto Nullam dignissim euismod risus, a molestieorci pulvinar in. Nullam egestas sollicitudin neque, nec vulput ate felis commodo sed. Suspendisse potenti. Duis bibendum orci leo. Praesent pharetra faucibus tellus, vel facilisis arcu commodo eget. Aliquam in tellus vel urna posuere consectetur.Vestibulum convallis cursus sodales. Donec purus sem, sodales faucibus malesuada et, feugiat id tortor.</p>
    <p>Nullam dignissim euismod risus, a molestieorci pulvinar in. Nullam egestas sollicitudin neque, nec vulputate felis commodo sed. Suspendisse potenti. Duis bibendum orci leo. Praesent pharetra faucibus tellus, vel facilisis arcu commodo eget.</p>
  </section>

  <aside class="industries">
    <h2>Custom Industry Solutions</h2>
    <ul>
      <li>Custom Industry Solutions</li><li>Government</li><li>Medical</li><li>Fitness</li><li>Martial Arts</li><li>Alarm Monitoring</li><li>Property Management</li>
    </ul>
  </aside>

  <div class="divider"></div>

  <section class="intro">
    <h1>Payment Processing for the 21st Century.</h1>
    <div class="lead">TrulaPay provides the software, technology, and platform for multi-channel payment acceptance.</div>
    <p>Since 1992 we have been helping merchants streamline their payment acceptance. Whether your acceptance needs are online, at the poin-of-sale, or mobile; TrulaPay can help.</p>
    <p>We provide both “out-of -the-box ” and custom solutions for your company or organization to begin taking paymentsin line with your needs and desires.</p>
  </section>

  <section class="ach">
    <h2>ACH Payment Processing</h2>
    <div class="ach-cols">
      <div class="ach-col">
        <h3>Payment Gateway</h3>
        <div class="ach-photo photo-gateway" role="img" aria-label="Photo of a delighted customer holding cash"></div>
        <p>Lorem ipsum dolor sit amet, consectetur adipisci elit. Etiam non arcu a sapien curs sodales vivam euismod dui at turpis lacinia non</p>
      </div>
      <div class="ach-col">
        <h3>ACH Payment API</h3>
        <div class="ach-photo photo-api" role="img" aria-label="Photo of a business team in a bright office"></div>
        <p>Lorem ipsum dolor sit amet, consectetur adipisci elit. Etiam non arcu a sapien curs sodales vivam euismod dui at turpis lacinia non</p>
      </div>
      <div class="ach-col">
        <h3>Processing For Software Development</h3>
        <div class="ach-photo photo-dev" role="img" aria-label="Photo of a woman pointing at a laptop screen"></div>
        <p>Lorem ipsum dolor sit amet, consectetur adipisci elit. Etiam non arcu a sapien curs sodales vivam euismod dui at turpis lacinia non</p>
      </div>
    </div>
  </section>

  <footer class="site-footer">
    <p>© 2013 TrulaPay. Terms &amp; Conditions &nbsp;|&nbsp; Privacy Policy &nbsp;|&nbsp; Contact Us</p>
    <div class="socials"><span></span><span></span><span></span></div>
  </footer>
</body>
</html>
```